Podcast cover art (not a logo)

I’m launching an audio-only podcast for parents of neurodivergent children. The podcast is meant to feel like a calm, trusted professional voice — not a brand or a performance.

Style direction:
--Clean and minimal
--Calm and grounded
--Professional, not playful
--Nothing flashy, loud, or busy
--No cartoon imagery

Content on the cover:
--Podcast title: Under the Quiet Surface
--Subtitle or tagline: Supporting Neurodivergent Kids with Science, Not Shame (or Understanding Neurodivergent Kids)
--No episode numbers, no dates

Design preferences:
--Text-forward design
--Neutral or soft colors (muted blues, grays, off-whites)
--High contrast for readability at small sizes
--Simple, timeless font

What I do NOT want:
--A logo or branding system
--Illustrations of children or families
--Bright colors or playful graphics
--Trendy fonts or visual effects

Technical requirements:
--Square image
--3000 × 3000 pixels
--RGB color mode
--JPEG or PNG
--File size under 500 KB

Deliverables:
--Final cover art file
--Optional: one or two alternate background color versions

```html
<!DOCTYPE html>
<html lang="en">
<head>
<meta charset="utf-8">
<title>Under the Quiet Surface — Podcast Cover</title>
<link href="https://fonts.googleapis.com/css2?family=Anton&family=Poppins:wght@300&display=swap" rel="stylesheet">
<style>
  :root {
    --page-bg: #e7e8ea;
    --cover-top: #3e5060;
    --cover-mid: #7b8a96;
    --cover-bottom: #adb6be;
    --mist: rgba(190, 215, 232, 0.28);
    --title-ink: #121a22;
    --subtitle-ink: #f4f6f8;
    --tagline-ink: #4a4d52;
    --rule: #4f5257;
  }
  * { margin: 0; padding: 0; box-sizing: border-box; }
  html, body {
    width: 1200px;
    height: 1082px;
    overflow: hidden;
    background: var(--page-bg);
  }
  .cover {
    position: absolute;
    left: 179px;
    top: 120px;
    width: 842px;
    height: 842px;
    overflow: hidden;
    background:
      radial-gradient(ellipse 420px 260px at 78% 72%, var(--mist), transparent 70%),
      radial-gradient(ellipse 380px 220px at 30% 40%, rgba(170, 200, 220, 0.18), transparent 70%),
      radial-gradient(ellipse 300px 180px at 88% 12%, rgba(120, 160, 190, 0.25), transparent 70%),
      linear-gradient(180deg, var(--cover-top) 0%, var(--cover-mid) 42%, var(--cover-bottom) 100%);
  }
  .title {
    position: absolute;
    left: 0;
    top: 170px;
    width: 100%;
    text-align: center;
    font-weight: normal;
  }
  .title-main {
    display: block;
    font-family: "Anton", Impact, sans-serif;
    font-size: 210px;
    line-height: 1.05;
    letter-spacing: 2px;
    color: var(--title-ink);
  }
  .title-sub {
    display: block;
    margin-top: 18px;
    font-family: "Poppins", Arial, sans-serif;
    font-weight: 300;
    font-size: 56px;
    line-height: 1.1;
    letter-spacing: 1px;
    color: var(--subtitle-ink);
  }
  .tagline {
    position: absolute;
    left: 379px;
    top: 670px;
    padding-left: 19px;
    border-left: 3px solid var(--rule);
    font-family: "Poppins", Arial, sans-serif;
    font-weight: 300;
    font-size: 27px;
    line-height: 37px;
    color: var(--tagline-ink);
    white-space: nowrap;
  }
</style>
</head>
<body>
  <main class="cover">
    <h1 class="title">
      <span class="title-main">Under</span>
      <span class="title-sub">the Quiet Surface</span>
    </h1>
    <p class="tagline">Supporting<br>Neurodivergent Kids with<br>Science, Not Shame</p>
  </main>
</body>
</html>
```